Website Design For digital agency

We have an existing website called www.qlmr.co.uk which needs revamping. We are currently using the Duda web builder platform to build our website so we need someone to create or combine our existing pages into a user friends, modern design. We will need design assets for our internal team to implement. Here is a link to our support if you have any question regarding the the website builder or image sizes and available design widgets. https://help.pagevantor.com/hc/en-us/articles/480027155302-Image-Size-Guidelines

Target Market(s)

Small to medium businesses looking for revamps and new designs

Industry/Entity Type

Website

Number of Pages Required

5+ page

Other font styles liked:
• Publica

Colors
33a6d7
3377b5
886aae

Requirements
Must have
• separate pages to outline the services we provide.

```html
<!DOCTYPE html>
<html lang="en">
<head>
<meta charset="utf-8">
<title>Quillmere Media — Digital Agency</title>
<link rel="stylesheet" href="https://fonts.googleapis.com/css2?family=Poppins:wght@300;400;500;600;700;800&display=swap">
<style>
:root{
  --blue:#1f8ce8;
  --blue-bright:#2496f2;
  --blue-soft:#dbeeff;
  --blue-mid:#3fa9f5;
  --navy:#22399a;
  --navy-dark:#0d1b3f;
  --orange:#ffb300;
  --white:#ffffff;
  --line:#c9d6ea;
  --text:#2b3f93;
}
*{box-sizing:border-box;margin:0;padding:0}
html,body{width:1200px;height:3125px;overflow:hidden;background:var(--white)}
body{font-family:"Poppins",sans-serif;color:var(--text)}
.canvas{position:relative;width:1200px;height:3125px;overflow:hidden}
.backdrop{position:absolute;left:0;top:0}
.abs{position:absolute}

/* header */
.brand{left:130px;top:44px;display:flex;align-items:center;gap:12px}
.brand-dot{width:66px;height:66px;border-radius:50%;background:var(--white)}
.brand-name{font-size:24px;font-weight:700;color:var(--white);letter-spacing:1px}
.login{left:1026px;top:14px;font-size:12px;color:var(--navy);display:flex;align-items:center;gap:5px}
.nav{left:664px;top:76px;display:flex;align-items:center;gap:21px;font-size:12px;color:var(--navy)}
.nav .active{color:var(--navy);position:relative}
.nav .active::after{content:"";position:absolute;left:0;right:0;top:26px;height:3px;background:var(--orange);border-radius:2px}
.btn-solid{background:var(--blue);color:var(--white);font-size:10px;font-weight:600;display:inline-flex;align-items:center;justify-content:center;border-radius:2px}
.btn-line{border:1.5px solid var(--navy);color:var(--navy);font-size:10px;font-weight:600;display:inline-flex;align-items:center;justify-content:center;border-radius:2px;background:var(--white)}

/* hero */
.hero-kicker{left:129px;top:292px;font-size:32px;font-weight:400;color:var(--navy);line-height:1.1}
.hero-title{left:129px;top:327px;font-size:35px;font-weight:800;color:var(--blue);letter-spacing:.5px;line-height:1.1}
.hero-tag{left:130px;top:368px;font-size:14px;font-weight:300;color:var(--navy);letter-spacing:.6px}
.hero-art{left:616px;top:166px;width:454px;height:323px;border-radius:48% 52% 44% 56% / 55% 45% 55% 45%;background:linear-gradient(135deg,#2a97f0,#1a7fde 60%,#f0b52a 100%)}

/* sections */
.section-title{left:0;width:1200px;text-align:center;font-weight:600;color:var(--navy)}
.about-copy{left:166px;top:643px;width:868px;font-size:14.5px;line-height:22px;text-align:center;color:var(--text)}
.chev{left:588px;width:24px;height:14px}

.services-art{left:467px;top:1059px;width:268px;height:182px;border-radius:50%;background:radial-gradient(circle,#e8f4ff 0%,#9ccc4a 35%,#2d8fa3 65%,rgba(31,140,232,0) 75%)}
.services-title{left:0;top:1252px;width:1200px;text-align:center;font-size:28px;font-weight:300;color:var(--white)}
.services-title b{font-weight:600}
.services-rule{left:585px;top:1298px;width:30px;height:3px;background:var(--white)}
.services-lead{left:150px;top:1310px;width:900px;text-align:center;font-size:14.5px;line-height:22px;color:var(--white)}
.service{width:290px;text-align:center;color:var(--white)}
.service svg{display:block;margin:0 auto}
.service h3{font-size:15px;font-weight:600;margin-top:18px;letter-spacing:.3px}
.service h4{font-size:13px;font-weight:400;letter-spacing:.2px}
.service p{font-size:14px;line-height:21px;margin-top:9px}

/* contact */
.col-head{font-size:18px;font-weight:600;color:var(--navy)}
.col-rule{height:1px;width:36px;background:var(--line)}
.info-icon{width:54px;height:54px;border-radius:50%;background:var(--blue);display:flex;align-items:center;justify-content:center}
.info-label{font-size:13px;font-weight:600;color:var(--navy)}
.info-text{font-size:10.5px;color:var(--navy);line-height:18px}
.contact-lead{left:592px;top:2290px;font-size:13.5px;line-height:21px;color:var(--navy)}
.field{border:1px solid var(--line);display:flex;align-items:center;font-size:11px;color:var(--navy);background:var(--white)}
.field .ico{width:36px;height:100%;border-right:1px solid var(--line);display:flex;align-items:center;justify-content:center}
.field span{padding-left:12px}
.field.message{align-items:flex-start}
.field.message .ico{height:36px;border-right:none}
.field.message span{padding-top:11px}
.check{left:593px;top:2565px;width:205px;height:52px;border:1px solid #d3d3d3;background:#f9f9f9;display:flex;align-items:center;font-size:10.5px;color:#222;font-weight:500}
.check .box{width:22px;height:22px;border:2px solid #c1c1c1;background:var(--white);margin:0 10px 0 13px;border-radius:2px}
.check .badge{margin-left:auto;margin-right:12px;width:26px;height:26px;background:#c9d3e6;border-radius:3px}
.submit{left:593px;top:2633px;width:141px;height:40px;background:var(--blue);color:var(--white);font-size:13px;font-weight:600;display:flex;align-items:center;justify-content:center;border-radius:3px}

/* footer */
.foot-mark{left:545px;top:2776px;width:110px;height:110px;border-radius:50%;background:var(--white);display:flex;align-items:center;justify-content:center}
.foot-mark i{width:88px;height:88px;border-radius:50%;background:var(--blue);display:block}
.foot-col{top:2942px;color:var(--white)}
.foot-col h5{font-size:12px;font-weight:600;margin-bottom:8px;letter-spacing:.3px}
.foot-col li{list-style:none;font-size:10px;line-height:18px}
.foot-divider{top:2944px;width:1px;height:105px;background:rgba(255,255,255,.35)}
.social{display:flex;gap:8px}
.social i{width:24px;height:24px;border:1px solid var(--white);border-radius:50%;display:block}
.sub-field{width:161px;height:26px;border:1px solid var(--white);font-size:10px;color:var(--white);display:flex;align-items:center;padding-left:10px;border-radius:2px}
.sub-btn{width:103px;height:27px;border:1px solid var(--white);font-size:10px;font-weight:600;color:var(--white);display:flex;align-items:center;justify-content:center;border-radius:2px}
.legal{left:0;top:3092px;width:1200px;height:33px;background:var(--navy-dark);color:var(--white);font-size:10.5px;display:flex;align-items:center;justify-content:center}
</style>
</head>
<body>
<div class="canvas">

  <svg class="backdrop" width="1200" height="3125" viewBox="0 0 1200 3125" aria-hidden="true">
    <path d="M0,0 H760 C700,20 600,60 520,140 C460,200 400,240 300,228 C190,215 90,170 0,196 Z" fill="#1f8ce8"/>
    <path d="M0,0 H120 C80,20 40,30 0,30 Z" fill="#3fa9f5"/>
    <!-- services band -->
    <path d="M0,995 C140,1050 260,1010 400,975 C520,945 600,950 720,975 C880,1005 1020,985 1200,1000 V2120 C1050,2090 900,2150 740,2120 C560,2090 380,2030 200,2070 C120,2085 50,2110 0,2110 Z" fill="#dbeeff"/>
    <path d="M0,1040 C120,1100 260,1045 400,990 C480,962 560,958 660,982 C820,1020 960,1085 1200,1052 V1990 C1060,2050 920,2050 780,2010 C630,1965 500,2020 360,2050 C230,2075 110,2040 0,2030 Z" fill="#1f8ce8"/>
    <path d="M0,1905 C180,1930 380,1960 560,1990 C700,2010 820,2040 960,2000 C1060,1972 1140,1960 1200,1965 V1990 C1060,2050 920,2050 780,2010 C630,1965 500,2020 360,2050 C230,2075 110,2040 0,2030 Z" fill="#2496f2"/>
    <path d="M0,1300 C80,1400 120,1560 70,1680 C45,1745 15,1800 0,1830 Z" fill="#ffb300"/>
    <path d="M1200,1125 C1120,1175 1070,1300 1078,1400 C1088,1500 1150,1560 1200,1590 Z" fill="#3fa9f5"/>
    <!-- footer -->
    <path d="M0,2795 C150,2770 320,2790 470,2830 C620,2870 760,2830 900,2800 C1020,2775 1120,2780 1200,2790 V2930 H0 Z" fill="#dbeeff"/>
    <path d="M0,2860 C200,2910 400,2945 600,2925 C800,2905 1000,2875 1200,2885 V3125 H0 Z" fill="#1f8ce8"/>
  </svg>

  <!-- header -->
  <div class="abs brand"><span class="brand-dot"></span><span class="brand-name">QUILLMERE MEDIA</span></div>
  <div class="abs login">
    <svg width="11" height="11" viewBox="0 0 12 12"><circle cx="6" cy="4" r="2.6" fill="none" stroke="#ffb300" stroke-width="1.2"/><path d="M1.5,11.5 C2,8 10,8 10.5,11.5" fill="none" stroke="#ffb300" stroke-width="1.2"/></svg>Login
  </div>
  <nav class="abs nav">
    <svg width="13" height="13" viewBox="0 0 14 14"><circle cx="6" cy="6" r="4.3" fill="none" stroke="#22399a" stroke-width="1.8"/><path d="M9.2,9.2 L13,13" stroke="#22399a" stroke-width="1.8"/></svg>
    <span class="active">Home</span><span>Services</span><span>About</span><span>Blog</span><span>Contact Us</span>
    <span class="btn-solid" style="width:79px;height:22px">GET QUOTE</span>
  </nav>

  <!-- hero -->
  <div class="abs hero-kicker">LET US HELP YOU</div>
  <div class="abs hero-title">GROW YOUR BUSINESS!</div>
  <div class="abs hero-tag">Making your Business better is our priority.</div>
  <span class="abs btn-solid" style="left:130px;top:403px;width:94px;height:28px">GET QUOTE</span>
  <span class="abs btn-line" style="left:238px;top:403px;width:114px;height:28px">OUR SERVICES</span>
  <div class="abs hero-art" role="img" aria-label="Illustration of two people presenting growth charts around a large gear and monitor"></div>

  <!-- about -->
  <h2 class="abs section-title" style="top:592px;font-size:26px">ABOUT US</h2>
  <p class="abs about-copy">Lorem ipsum dolor sit amet, consectetur adipiscing elit, sed do eiusmod tempor incididunt ut labore et dolore magna aliqua. Quis ipsum suspendisse ultrices gravida. Risus commodo viverra maecenas accumsan lacus vel facilisis. Lorem ipsum dolor sit amet, consectetur adipiscing elit, sed do eiusmod tempor incididunt ut labore et dolore magna aliqua. Quis ipsum suspendisse ultrices gravida. Risus commodo viverra maecenas accumsan lacus vel facilisis. Lorem ipsum dolor sit amet, consectetur adipiscing elit, sed do eiusmod tempor incididunt ut labore et dolore magna aliqua. Quis ipsum suspendisse ultrices gravida. Risus commodo viverra maecenas accumsan lacus vel facilisis.</p>
  <span class="abs btn-line" style="left:552px;top:794px;width:95px;height:27px">ABOUT US</span>
  <svg class="abs chev" style="top:866px" viewBox="0 0 24 14"><path d="M2,2 L12,12 L22,2" fill="none" stroke="#22399a" stroke-width="2.5"/></svg>

  <!-- services -->
  <div class="abs services-art" role="img" aria-label="Illustration of a monitor surrounded by marketing icons"></div>
  <h2 class="abs services-title">SOME OF OUR <b>SERVICES</b></h2>
  <div class="abs services-rule"></div>
  <p class="abs services-lead">We know the internet like the back of our smartphone, and we provide you with the full gamut of digital marketing services, everything from Website &amp; traffic building to social media campaign construction.</p>

  <div class="abs service" style="left:109px;top:1402px">
    <svg width="92" height="88" viewBox="0 0 92 88" fill="none" stroke="#fff" stroke-width="2.5"><path d="M10,60 L40,40 L46,70 Z"/><circle cx="38" cy="12" r="10"/><rect x="64" y="2" width="22" height="22" rx="2"/><rect x="62" y="46" width="22" height="22" rx="2"/><rect x="4" y="18" width="18" height="26"/><path d="M6,80 H60"/></svg>
    <h3>SOCIAL MEDIA</h3><h4>MARKETING</h4>
    <p>Reach thousands of potential new customers online</p>
  </div>
  <div class="abs service" style="left:455px;top:1402px">
    <svg width="92" height="88" viewBox="0 0 92 88" fill="none" stroke="#fff" stroke-width="2.5"><rect x="12" y="4" width="74" height="80" rx="3"/><path d="M12,20 H4 V80 C4,84 8,84 12,84"/><path d="M24,16 H74 M24,28 H74"/><rect x="24" y="38" width="22" height="30"/><path d="M54,40 H74 M54,50 H74 M54,60 H74 M24,76 H74"/></svg>
    <h3>PRESS RELEASE</h3><h4>CONTENT DISTRIBUTION</h4>
    <p>Great way to put your products and services on display</p>
  </div>
  <div class="abs service" style="left:799px;top:1402px">
    <svg width="92" height="88" viewBox="0 0 92 88" fill="none" stroke="#fff" stroke-width="2.5"><rect x="4" y="4" width="84" height="80" rx="3"/><path d="M4,16 H88"/><path d="M14,50 L32,34 L50,48 L72,26"/><circle cx="32" cy="34" r="4"/><circle cx="50" cy="48" r="4"/><circle cx="72" cy="26" r="4"/><path d="M20,84 V62 M36,84 V56 M52,84 V66 M68,84 V52"/></svg>
    <h3>SEO</h3><h4>MANAGEMENT</h4>
    <p>Every managed SEO plan is custom to fit your needs</p>
  </div>

  <div class="abs service" style="left:109px;top:1652px">
    <svg width="92" height="88" viewBox="0 0 92 88" fill="none" stroke="#fff" stroke-width="2.5"><rect x="8" y="4" width="76" height="80" rx="2"/><path d="M8,14 H84"/><rect x="18" y="24" width="34" height="24"/><path d="M18,56 H60 M18,64 H60 M18,72 H60"/><path d="M70,24 V76 L74,82 L78,76 V24 Z"/></svg>
    <h3>BLOG WRITING</h3><h4>CONTENT MANAGEMENT</h4>
    <p>High quality content direct to your site each month.</p>
  </div>
  <div class="abs service" style="left:455px;top:1645px">
    <svg width="92" height="95" viewBox="0 0 92 95" fill="none" stroke="#fff" stroke-width="2.5"><path d="M20,62 C6,62 2,48 10,40 C8,26 24,20 32,26 C38,8 64,8 68,26 C84,24 92,44 80,56"/><rect x="24" y="38" width="40" height="32" rx="2"/><path d="M24,46 H64 M38,60 L34,56 L38,52 M50,52 L54,56 L50,60 M46,50 L42,62"/><path d="M44,70 V86 M34,88 H54 M78,48 V70 M72,54 L78,48 L84,54"/></svg>
    <h3>WEB SERVICES</h3>
    <p style="margin-top:30px">combination of bespoke design &amp; development to produce beautiful websites that your audience will absolutely love.</p>
  </div>
  <div class="abs service" style="left:799px;top:1648px">
    <svg width="110" height="90" viewBox="0 0 110 90" fill="none" stroke="#fff" stroke-width="2.5"><rect x="4" y="4" width="102" height="66" rx="3"/><path d="M4,58 H106 M44,70 L40,84 M66,70 L70,84 M30,86 H80"/><path d="M24,50 V26 L30,16 L36,26 V50 Z M46,50 V20 H56 V50 M66,50 V28 L76,50 Z M84,50 V36 H94 V50"/></svg>
    <h3>GRAPHIC DESIGN</h3>
    <p style="margin-top:30px">Our team can deliver art direction and sketches to make your product stand out from the crowd.</p>
  </div>

  <svg class="abs chev" style="top:2006px" viewBox="0 0 24 14"><path d="M2,2 L12,12 L22,2" fill="none" stroke="#ffffff" stroke-width="2.5"/></svg>

  <!-- contact -->
  <h2 class="abs section-title" style="top:2155px;font-size:26px">LET'S WORK TOGETHER!</h2>

  <div class="abs col-head" style="left:131px;top:2243px">CONTACT INFO</div>
  <div class="abs col-rule" style="left:131px;top:2280px"></div>

  <div class="abs info-icon" style="left:130px;top:2298px"><svg width="20" height="24" viewBox="0 0 20 24"><path d="M10,1 C4,1 1,5 1,9 C1,15 10,23 10,23 C10,23 19,15 19,9 C19,5 16,1 10,1 Z" fill="none" stroke="#fff" stroke-width="2"/><circle cx="10" cy="9" r="3" fill="#fff"/></svg></div>
  <div class="abs info-label" style="left:199px;top:2297px">QUILLMERE MEDIA</div>
  <div class="abs info-text" style="left:199px;top:2316px">Hubspace 4 Larkfield St,<br>London, EC1V 7QT</div>

  <div class="abs info-icon" style="left:130px;top:2380px"><svg width="22" height="22" viewBox="0 0 22 22"><path d="M5,2 L8,2 L10,7 L7.5,9 C9,12 10,13 13,14.5 L15,12 L20,14 V17 C20,19 18,20 16,20 C9,19 3,13 2,6 C2,4 3,2 5,2 Z" fill="none" stroke="#fff" stroke-width="2"/></svg></div>
  <div class="abs info-label" style="left:199px;top:2390px">PHONE</div>
  <div class="abs info-text" style="left:199px;top:2408px">5550-1400-1921</div>

  <div class="abs info-icon" style="left:130px;top:2460px"><svg width="24" height="18" viewBox="0 0 24 18"><rect x="1" y="1" width="22" height="16" rx="1.5" fill="none" stroke="#fff" stroke-width="2"/><path d="M1,2 L12,10 L23,2" fill="none" stroke="#fff" stroke-width="2"/></svg></div>
  <div class="abs info-label" style="left:199px;top:2470px">EMAIL</div>
  <div class="abs info-text" style="left:199px;top:2489px">info@qlmr.co.uk</div>

  <div class="abs col-head" style="left:592px;top:2243px">CONTACT US</div>
  <div class="abs col-rule" style="left:592px;top:2280px"></div>
  <p class="abs contact-lead">Have a question or need more information?<br>Give us a call or use the form below</p>

  <div class="abs field" style="left:593px;top:2367px;width:232px;height:37px"><div class="ico"><svg width="12" height="12" viewBox="0 0 12 12"><circle cx="6" cy="3.5" r="3" fill="#ffb300"/><path d="M0,12 C0,7 12,7 12,12 Z" fill="#ffb300"/></svg></div><span>First Name*</span></div>
  <div class="abs field" style="left:837px;top:2367px;width:232px;height:37px"><div class="ico"><svg width="12" height="12" viewBox="0 0 12 12"><circle cx="6" cy="3.5" r="3" fill="#ffb300"/><path d="M0,12 C0,7 12,7 12,12 Z" fill="#ffb300"/></svg></div><span>Last Name*</span></div>
  <div class="abs field" style="left:593px;top:2417px;width:232px;height:37px"><div class="ico"><svg width="12" height="12" viewBox="0 0 22 22"><path d="M5,2 L8,2 L10,7 L7.5,9 C9,12 10,13 13,14.5 L15,12 L20,14 V17 C20,19 18,20 16,20 C9,19 3,13 2,6 C2,4 3,2 5,2 Z" fill="#ffb300"/></svg></div><span>Your Phone*</span></div>
  <div class="abs field" style="left:837px;top:2417px;width:232px;height:37px"><div class="ico"><svg width="13" height="10" viewBox="0 0 24 18"><rect x="0" y="0" width="24" height="18" rx="2" fill="#ffb300"/><path d="M1,2 L12,10 L23,2" fill="none" stroke="#fff" stroke-width="2"/></svg></div><span>Your Email*</span></div>
  <div class="abs field message" style="left:593px;top:2467px;width:476px;height:84px"><div class="ico"><svg width="12" height="12" viewBox="0 0 12 12"><circle cx="6" cy="6" r="5.5" fill="#ffb300"/><circle cx="3.5" cy="6" r="1" fill="#fff"/><circle cx="6" cy="6" r="1" fill="#fff"/><circle cx="8.5" cy="6" r="1" fill="#fff"/></svg></div><span>Your Message*</span></div>

  <div class="abs check"><span class="box"></span>I'm not a robot<span class="badge" role="img" aria-label="HumanCheck badge"></span></div>
  <div class="abs submit">SUBMIT</div>

  <!-- footer -->
  <div class="abs foot-mark"><i role="img" aria-label="Quillmere Media mark"></i></div>

  <div class="abs foot-col" style="left:130px"><h5>NAVIGATE</h5><ul><li>Home</li><li>About</li><li>Service</li><li>Blog</li><li>Contact</li></ul></div>
  <div class="abs foot-divider" style="left:240px"></div>
  <div class="abs foot-col" style="left:277px"><h5>SERVICES</h5><ul><li>Website Development &amp; Hosting</li><li>SEO &amp; Content management</li><li>PPC Management</li><li>Reviews &amp; Reputation Management</li><li>Social Media Marketing</li></ul></div>
  <div class="abs foot-divider" style="left:501px"></div>
  <div class="abs foot-col" style="left:541px"><h5>CONTACT US</h5><ul><li>☏&nbsp; (555) 014-0192</li><li>✉&nbsp; info@qlmr.co.uk</li><li style="margin-top:18px;padding-left:17px;text-indent:-17px">⌖&nbsp; Hubspace 4 Larkfield St,<br>London, EC1V 7QT</li></ul></div>
  <div class="abs foot-divider" style="left:707px"></div>
  <div class="abs foot-col" style="left:746px"><h5>FOLLOW US</h5><div class="social" aria-label="Social links"><i></i><i></i><i></i></div></div>
  <div class="abs foot-divider" style="left:871px"></div>
  <div class="abs foot-col" style="left:908px"><h5>SUBSCRIBE</h5>
    <div class="sub-field">Name</div>
    <div class="sub-field" style="margin-top:9px">Email</div>
    <div class="sub-btn" style="margin-top:11px">SUBSCRIBE</div>
  </div>

  <div class="abs legal">© Copyright 2019 Quillmere Media Limited trading as Quillmere Media| Registered in England and Wales. Registered Number: 04417263. Privacy Policy</div>
</div>
</body>
</html>
```